Banner Ad Design Project for responsive website

Looking to update the main banner on my website www.bridalpathly.com but it will be for our new responsive website, you can see here http://www.bridalpathly.com/dev/
Banner should be 300 px high by1920 pix wide
Please contact me with any questions
Should include:
All the text from the existing banner ie
Bridal Show
THE FIRST 50 BRIDES WILL GET A CHANCE TO WIN $25000
Honeymoon Cruise Giveaway
"Pick the Perfect Gown" casting call
Banner should be 1920 pix wide
Final delivery will require layered psd file and all fonts

Target Market(s)

Brides

Industry/Entity Type

Call

Requirements
Must have
• All the text from the existing banner ie
• Bridal Show
• THE FIRST 50 BRIDES WILL GET A CHANCE TO WIN $25000
• Honeymoon Cruise Giveaway
• "Pick the Perfect Gown" casting call
• Banner should be 1920 pix wide
Nice to have
• The look and feel of our postcard, see attached
Should not have
• Any specifics to any date/time/location as the banner will be online all the time and the specifics for each show will be different

```html
<!DOCTYPE html>
<html lang="en">
<head>
<meta charset="utf-8">
<title>Bridal Show Banner</title>
<link rel="stylesheet" href="https://fonts.googleapis.com/css2?family=Great+Vibes&family=Open+Sans:wght@400;600;700&display=swap">
<style>
  :root {
    --page-bg: #1e1e1e;
    --cream-light: #fbf8f2;
    --cream-mid: #f1e7da;
    --cream-warm: #e8d6c2;
    --sky-blue: #4aa8ee;
    --royal-blue: #0b3f8e;
    --ink: #2b2b2b;
    --panel: rgba(255,255,255,0.72);
    --sea-top: #1f8fc7;
    --sea-bottom: #5cc3e0;
    --photo-ivory: #f2ede4;
    --photo-warm: #e2d6c6;
    --photo-skin: #d8c3ad;
    --photo-dark: #2a353b;
    --dash: rgba(255,255,255,0.9);
    --rule: #bdb3a6;
  }
  * { margin: 0; padding: 0; box-sizing: border-box; }
  html, body {
    width: 1200px; height: 734px; overflow: hidden;
    background: var(--page-bg);
    font-family: "Open Sans", Arial, sans-serif;
  }
  .banner {
    position: absolute; left: 94px; top: 258px;
    width: 1014px; height: 158px; overflow: hidden;
    background: linear-gradient(90deg, var(--cream-warm) 0%, var(--cream-mid) 18%, var(--cream-light) 45%, var(--cream-light) 62%, var(--cream-mid) 100%);
  }
  .hero-photo {
    position: absolute; left: 590px; top: 0; width: 424px; height: 158px;
    background: linear-gradient(90deg,
      rgba(242,237,228,0) 0%,
      var(--photo-ivory) 16%,
      var(--photo-warm) 42%,
      var(--photo-skin) 62%,
      #6d6e6a 80%,
      var(--photo-dark) 92%,
      var(--photo-dark) 100%);
  }
  .cut-frame {
    position: absolute; left: 6px; top: 6px; right: 7px; bottom: 8px;
    border: 1px dashed var(--dash);
    pointer-events: none;
  }
  .show-title {
    position: absolute; left: 20px; top: 16px;
    font-family: "Great Vibes", cursive; font-size: 56px; font-weight: 400; line-height: 1;
    white-space: nowrap;
  }
  .show-title .word-bridal { color: var(--sky-blue); }
  .show-title .word-show { color: var(--royal-blue); }
  .title-rule {
    position: absolute; left: 22px; top: 81px; width: 274px;
    border-top: 1px dotted var(--rule);
  }
  .offer {
    position: absolute; left: 22px; top: 90px; width: 280px;
    color: var(--ink); text-transform: uppercase; line-height: 1;
  }
  .offer-line { display: block; white-space: nowrap; }
  .offer-line.first { font-size: 12px; font-weight: 400; }
  .offer-line.first strong { font-size: 19px; font-weight: 700; }
  .offer-line.second { margin-top: -2px; padding-left: 9px; font-size: 12px; }
  .offer-line.second strong { font-size: 19px; font-weight: 700; }
  .offer .prize {
    font-size: 35px; font-weight: 700; color: var(--sky-blue);
    text-shadow: 0 1px 0 #fff;
  }
  .cruise-panel {
    position: absolute; left: 324px; top: 18px; width: 264px; height: 93px;
    background: var(--panel);
  }
  .cruise-photo {
    position: absolute; left: 7px; top: 5px; width: 116px; height: 84px;
    background: linear-gradient(180deg, var(--sea-top) 0%, #3aa7d6 55%, var(--sea-bottom) 100%);
  }
  .cruise-text {
    position: absolute; left: 133px; top: 26px; color: var(--royal-blue);
  }
  .cruise-text .script {
    display: block; font-family: "Great Vibes", cursive; font-size: 24px; line-height: 1;
  }
  .cruise-text .label {
    display: block; font-size: 14.5px; font-weight: 600; line-height: 1.2; white-space: nowrap;
  }
  .casting-call {
    position: absolute; left: 328px; top: 120px;
    color: var(--royal-blue); white-space: nowrap;
  }
  .casting-call .lead { font-size: 10.5px; font-weight: 600; }
  .casting-call .quote { font-size: 15px; }
  .casting-call em {
    font-family: "Great Vibes", cursive; font-style: normal; font-size: 19px;
  }
</style>
</head>
<body>
  <section class="banner" aria-label="Bridal Show banner">
    <div class="hero-photo" role="img" aria-label="Bride holding a white rose bouquet beside the groom"></div>

    <h1 class="show-title"><span class="word-bridal">Bridal</span> <span class="word-show">Show</span></h1>
    <div class="title-rule"></div>

    <p class="offer">
      <span class="offer-line first">The first <strong>50 Brides</strong> will get a</span>
      <span class="offer-line second"><strong>Chance</strong> to win <span class="prize">$25000</span></span>
    </p>

    <div class="cruise-panel">
      <div class="cruise-photo" role="img" aria-label="Cruise ship sailing on turquoise sea"></div>
      <p class="cruise-text">
        <span class="script">Honeymoon</span>
        <span class="label">Cruise Giveaway</span>
      </p>
    </div>

    <p class="casting-call">
      <span class="lead">Open Casting Call</span>
      <span class="quote">"Pick the <em>Perfect</em> <em>Gown</em>"</span>
    </p>

    <div class="cut-frame"></div>
  </section>
</body>
</html>
```